Website Design for my CNC machine Shop.

I need a new website for my Machining Company.

It can be a simple website that acts more like an "Online Business card" I has to highlight the services I provide and give Companies the confidence to engage my services.

I needs it to be a really modern or even a little futuristic promoting my Company.

I have just moved locations and have renovated the premises and would be great to let everyone know along with a new website.

If you can help with linking it to search engines to help get more exposure that would be great.

It needs to accommodate the three main services I provide which will include capacities of each machine (within that service) and maybe a couple images.
CNC Machining (5-axis, 3-axis)
EDM Wire cutting
3D Metal Printing
Along with home page and Contact page

I have two websites and you can use the txt from either/combination of these.
www.korvaltooling.com.au
(no longer do Laser Marking and etching but now do 3D metal Printing)
www.tarnquill.com.au

Happy to chat further with the designer

Company logo's provided.

For Images: I am happy to use Glimmerbay and can purchase any images you like
EDM Wire cut
https://www.glimmerbay-pics.com/search/edm-wire-cutting

CNC Machining:
https://www.glimmerbay-pics.com/search/vertical-cnc-machining
Don't use any with engines or motor vehicle parts

3D metal Printing
https://www.glimmerbay-pics.com/search/slm-metal-printing

Target Market(s)

Defence, Aerospace, Medical, HIgh Precision

Industry/Entity Type

Mechanical Engineering

Coding

Coded - Design and coding required

Number of Pages Required

5+ page

Requirements
Must have
• Home page, 3 services, Contacts. Can add image to each of the services

```html
<!DOCTYPE html>
<html lang="en">
<head>
<meta charset="utf-8">
<title>Korval Precision Machinists</title>
<link href="https://fonts.googleapis.com/css2?family=Montserrat:wght@400;500;600&family=Outfit:wght@700;800&display=swap" rel="stylesheet">
<style>
:root{
  --navy:#0c3347;
  --navy-deep:#0a2c3e;
  --green:#3dbf88;
  --text:#3f4a52;
  --white:#ffffff;
  --rule:rgba(255,255,255,.18);
}
*{box-sizing:border-box;margin:0;padding:0}
html,body{width:1200px;height:3531px;overflow:hidden}
body{font-family:"Montserrat",sans-serif;color:var(--text);background:var(--white);position:relative}
.site-header{position:absolute;top:0;left:0;width:1200px;height:85px;background:var(--white)}
.brand{position:absolute;left:110px;top:16px;display:flex;flex-direction:column}
.brand-name{font-family:"Montserrat",sans-serif;font-weight:600;font-size:38px;letter-spacing:3px;color:var(--navy);line-height:1}
.brand-tag{font-size:9px;letter-spacing:2.6px;color:var(--green);margin-top:4px;font-weight:500}
.main-nav{position:absolute;left:418px;top:0;height:85px;display:flex}
.main-nav a{display:flex;align-items:center;height:85px;padding:0 11px;font-size:15px;color:var(--navy);text-decoration:none;font-weight:500;margin-right:1px}
.main-nav a.active{background:var(--green);color:var(--white)}
.main-nav a.spaced{margin-left:12px}

.hero{position:absolute;top:85px;left:0;width:1200px;height:611px;
  background:radial-gradient(ellipse at 72% 40%,#6e6a5e 0%,#2c3b4f 35%,#16284a 65%,#0c1830 100%)}
.hero-copy{position:absolute;left:110px;top:210px;width:360px;text-align:center;color:var(--white)}
.hero-title{font-family:"Montserrat",sans-serif;font-weight:600;font-size:88px;letter-spacing:6px;line-height:1}
.hero-tag{font-size:21px;letter-spacing:6.5px;margin-top:12px}
.hero-lead{font-size:19px;line-height:27px;margin-top:26px;width:470px;margin-left:-55px}
.btn{display:inline-flex;align-items:center;justify-content:center;width:183px;height:47px;background:var(--green);color:var(--white);font-size:19px;text-decoration:none;font-weight:500}
.hero .btn{margin-top:28px}
.slider-arrow{position:absolute;top:282px;width:44px;height:44px}
.slider-arrow.prev{left:22px;opacity:.35}
.slider-arrow.next{left:1126px}

.service{position:absolute;left:0;width:1200px;height:670px}
.service-media{position:absolute;top:0;width:600px;height:670px}
.service-body{position:absolute;top:0;width:480px}
.service h2{font-family:"Outfit",sans-serif;font-weight:800;font-size:42px;color:var(--navy);line-height:1;margin-top:76px}
.service p{font-size:15px;line-height:27px;margin-top:18px}
.service p + p{margin-top:27px}
.service h3{font-family:"Outfit",sans-serif;font-weight:700;font-size:21px;color:var(--navy);margin-top:28px}
.features{list-style:none;margin-top:10px}
.features li{display:flex;align-items:center;font-size:15px;line-height:31px}
.features svg{width:15px;height:15px;margin-right:7px;flex:none}
.features.two-col{display:grid;grid-template-columns:200px 200px}
.service .btn{margin-top:38px}

.edm{top:696px}
.edm .service-media{left:0;background:linear-gradient(135deg,#cfd3d8 0%,#8a9199 45%,#4c535b 80%,#30363c 100%)}
.edm .service-body{left:623px}
.cnc{top:1366px}
.cnc .service-media{left:600px;background:linear-gradient(160deg,#e6e7e6 0%,#9c9e9c 40%,#3f4446 75%,#23282b 100%)}
.cnc .service-body{left:111px}
.printing{top:2036px}
.printing .service-media{left:0;background:radial-gradient(circle at 40% 50%,#c9dcf2 0%,#5b8fd1 35%,#1f55a8 70%,#0f3579 100%)}
.printing .service-body{left:623px}

.welcome{position:absolute;top:2706px;left:0;width:1200px;height:376px;text-align:center}
.welcome h2{font-family:"Outfit",sans-serif;font-weight:800;font-size:43px;color:var(--navy);margin-top:76px;line-height:1}
.welcome p{font-size:15px;line-height:27px;width:800px;margin:18px auto 0}
.welcome p + p{margin-top:27px}

.site-footer{position:absolute;top:3082px;left:0;width:1200px;height:449px;background:var(--navy);color:var(--white)}
.footer-brand{position:absolute;top:40px;left:0;width:1200px;text-align:center}
.footer-brand .name{font-family:"Montserrat",sans-serif;font-weight:600;font-size:110px;letter-spacing:12px;line-height:1}
.footer-brand .tag{font-size:28px;letter-spacing:8px;margin-top:14px}
.contact-row{position:absolute;top:213px;left:0;width:1200px;height:65px;border-top:1px solid var(--rule);border-bottom:1px solid var(--rule);display:flex}
.contact-item{display:flex;align-items:center;font-size:15px;line-height:27px}
.contact-item svg{flex:none;margin-right:14px}
.contact-item.address{width:473px;padding-left:172px;border-right:1px solid var(--rule)}
.contact-item.phone{width:231px;padding-left:42px;border-right:1px solid var(--rule)}
.contact-item.email{padding-left:42px}
.footer-nav{position:absolute;top:308px;left:0;width:1200px;text-align:center;font-size:15px;font-weight:500}
.footer-nav a{color:var(--white);text-decoration:none}
.footer-nav span{margin:0 14px}
.copyright{position:absolute;top:351px;left:0;width:1200px;text-align:center;font-size:15px}
.social{position:absolute;top:399px;left:0;width:1200px;display:flex;justify-content:center;gap:22px}
.social span{width:15px;height:15px;border-radius:50%;background:var(--green);display:block}
</style>
</head>
<body>
<header class="site-header">
  <div class="brand"><span class="brand-name">KORVAL</span><span class="brand-tag">PRECISION MACHINISTS</span></div>
  <nav class="main-nav">
    <a class="active" href="#">HOME</a>
    <a href="#">CNC MACHINING</a>
    <a class="spaced" href="#">EDM WIRE CUT</a>
    <a href="#">3D METAL PRINTING</a>
    <a class="spaced" href="#">CONTACT US</a>
  </nav>
</header>

<section class="hero" role="img" aria-label="Photo of a CNC spindle cutting metal with coolant hoses and flying swarf">
  <div class="hero-copy">
    <div class="hero-title">KORVAL</div>
    <div class="hero-tag">PRECISION MACHINISTS</div>
    <p class="hero-lead">We are an innovative company that Specialise in Technical and Creative Engineering.</p>
    <a class="btn" href="#">Read More</a>
  </div>
  <svg class="slider-arrow prev" viewBox="0 0 44 44"><circle cx="22" cy="22" r="20" fill="none" stroke="#fff" stroke-width="2"/><path d="M25 13l-9 9 9 9" fill="none" stroke="#fff" stroke-width="2"/></svg>
  <svg class="slider-arrow next" viewBox="0 0 44 44"><circle cx="22" cy="22" r="20" fill="none" stroke="#fff" stroke-width="2"/><path d="M19 13l9 9-9 9" fill="none" stroke="#fff" stroke-width="2"/></svg>
</section>

<section class="service edm">
  <div class="service-media" role="img" aria-label="Photo of an EDM wire cutting machine with a glowing spark at the cut"></div>
  <div class="service-body">
    <h2>EDM Wire Cut</h2>
    <p>We operate Swiss manufactured Vellmar EDM Machines which are regarded as the Aldermoor of wire cut machines.</p>
    <p>There is no limit to the hardness of material: as long as it is conductive we can cut it. Wire cut machines are extremely accurate and leave and incredibly smooth surface which is not possible with other cutting methods.</p>
    <h3>Some of the key features:</h3>
    <ul class="features">
      <li><svg viewBox="0 0 16 16"><circle cx="8" cy="8" r="8" fill="#3dbf88"/><path d="M4.3 8.2l2.5 2.5 5-5" fill="none" stroke="#fff" stroke-width="2"/></svg>5 - 10 micron accuracy</li>
      <li><svg viewBox="0 0 16 16"><circle cx="8" cy="8" r="8" fill="#3dbf88"/><path d="M4.3 8.2l2.5 2.5 5-5" fill="none" stroke="#fff" stroke-width="2"/></svg>30° taper cutting.</li>
      <li><svg viewBox="0 0 16 16"><circle cx="8" cy="8" r="8" fill="#3dbf88"/><path d="M4.3 8.2l2.5 2.5 5-5" fill="none" stroke="#fff" stroke-width="2"/></svg>400mm height</li>
      <li><svg viewBox="0 0 16 16"><circle cx="8" cy="8" r="8" fill="#3dbf88"/><path d="M4.3 8.2l2.5 2.5 5-5" fill="none" stroke="#fff" stroke-width="2"/></svg>550mm X 350mm X 400mm</li>
    </ul>
    <a class="btn" href="#">Read More</a>
  </div>
</section>

<section class="service cnc">
  <div class="service-body">
    <h2>CNC Machining</h2>
    <p>With our combination of high quality Okaru Machining Centres we are able to provide innovative solutions to your precision CNC machining requirements.</p>
    <p>Varying from general 2-D projects to more complex 3-D machining of prototypes and assemblies we are able to satisfy most medium size engineering requirements.</p>
    <h3>Some of the key features:</h3>
    <ul class="features">
      <li><svg viewBox="0 0 16 16"><circle cx="8" cy="8" r="8" fill="#3dbf88"/><path d="M4.3 8.2l2.5 2.5 5-5" fill="none" stroke="#fff" stroke-width="2"/></svg>Max Work piece size: 2m (l) X 800mm (w) X 500mm (h)</li>
      <li><svg viewBox="0 0 16 16"><circle cx="8" cy="8" r="8" fill="#3dbf88"/><path d="M4.3 8.2l2.5 2.5 5-5" fill="none" stroke="#fff" stroke-width="2"/></svg>Max Travel: 1000mm (l) X 500mm (w) X 500mm (h).</li>
      <li><svg viewBox="0 0 16 16"><circle cx="8" cy="8" r="8" fill="#3dbf88"/><path d="M4.3 8.2l2.5 2.5 5-5" fill="none" stroke="#fff" stroke-width="2"/></svg>12 000 rpm</li>
    </ul>
    <a class="btn" href="#">Read More</a>
  </div>
  <div class="service-media" role="img" aria-label="Photo of a vertical CNC mill cutting a part in a chuck with coolant spray"></div>
</section>

<section class="service printing">
  <div class="service-media" role="img" aria-label="Photo of a 3D printed metal lattice sphere on a stand in blue light"></div>
  <div class="service-body">
    <h2>3D Metal Printing</h2>
    <p>Stemming from an engineering background and are well accustomed to handling technical projects wether it be laser etching a gauge or a precise machined part.</p>
    <p>On the other hand we have a great deal of graphic design experience so helping in your creative project is right up our alley.</p>
    <h3>Some of the key features:</h3>
    <ul class="features two-col">
      <li><svg viewBox="0 0 16 16"><circle cx="8" cy="8" r="8" fill="#3dbf88"/><path d="M4.3 8.2l2.5 2.5 5-5" fill="none" stroke="#fff" stroke-width="2"/></svg>Aluminium</li>
      <li><svg viewBox="0 0 16 16"><circle cx="8" cy="8" r="8" fill="#3dbf88"/><path d="M4.3 8.2l2.5 2.5 5-5" fill="none" stroke="#fff" stroke-width="2"/></svg>Hard and Soft Woods</li>
      <li><svg viewBox="0 0 16 16"><circle cx="8" cy="8" r="8" fill="#3dbf88"/><path d="M4.3 8.2l2.5 2.5 5-5" fill="none" stroke="#fff" stroke-width="2"/></svg>Stainless Steel</li>
      <li><svg viewBox="0 0 16 16"><circle cx="8" cy="8" r="8" fill="#3dbf88"/><path d="M4.3 8.2l2.5 2.5 5-5" fill="none" stroke="#fff" stroke-width="2"/></svg>Plastics</li>
      <li><svg viewBox="0 0 16 16"><circle cx="8" cy="8" r="8" fill="#3dbf88"/><path d="M4.3 8.2l2.5 2.5 5-5" fill="none" stroke="#fff" stroke-width="2"/></svg>Titanium</li>
      <li><svg viewBox="0 0 16 16"><circle cx="8" cy="8" r="8" fill="#3dbf88"/><path d="M4.3 8.2l2.5 2.5 5-5" fill="none" stroke="#fff" stroke-width="2"/></svg>Leather</li>
    </ul>
    <a class="btn" href="#" style="margin-top:60px">Read More</a>
  </div>
</section>

<section class="welcome">
  <h2>Welcome to Korval</h2>
  <p>KORVAL is a quality driven mechanical engineering company. We provide a range of speciality services to a broad range of customers in the Automotive, Aerospace and Defence Industries.</p>
  <p>We are as diverse as our customer base, we are confident in providing an exceptionally high standard of quality in all facets of our company. Our factory is equipped with an extensive range of machinery allowing us to provide a full range of services such as wire and spark erosion, milling and turning.</p>
</section>

<footer class="site-footer">
  <div class="footer-brand"><div class="name">KORVAL</div><div class="tag">PRECISION MACHINISTS</div></div>
  <div class="contact-row">
    <div class="contact-item address">
      <svg width="20" height="26" viewBox="0 0 20 26"><path d="M10 0C4.5 0 0 4.4 0 9.8 0 17 10 26 10 26s10-9 10-16.2C20 4.4 15.5 0 10 0z" fill="#3dbf88"/><circle cx="10" cy="9.5" r="3.5" fill="#0c3347"/></svg>
      <span>Unit 4, 18 Brackenridge Rd,<br>ELMSTEAD, VIC 3999</span>
    </div>
    <div class="contact-item phone">
      <svg width="26" height="26" viewBox="0 0 24 24"><path d="M6.6 10.8a15.1 15.1 0 0 0 6.6 6.6l2.2-2.2a1 1 0 0 1 1-.25 11.4 11.4 0 0 0 3.6.57 1 1 0 0 1 1 1V20a1 1 0 0 1-1 1A17 17 0 0 1 3 4a1 1 0 0 1 1-1h3.5a1 1 0 0 1 1 1c0 1.25.2 2.45.57 3.57a1 1 0 0 1-.25 1z" fill="#3dbf88"/></svg>
      <span>+61 400 555 019</span>
    </div>
    <div class="contact-item email">
      <svg width="26" height="20" viewBox="0 0 26 20"><rect width="26" height="20" rx="2" fill="#3dbf88"/><path d="M1 2l12 9 12-9" fill="none" stroke="#0c3347" stroke-width="2"/></svg>
      <span>info@korvaltooling.com.au</span>
    </div>
  </div>
  <nav class="footer-nav"><a href="#">HOME</a><span>|</span><a href="#">CNC MACHINING</a><span>|</span><a href="#">EDM WIRE CUT</a><span>|</span><a href="#">3D METAL PRINTING</a><span>|</span><a href="#">CONTACT US</a></nav>
  <div class="copyright">© 2014 BY KORVAL.</div>
  <div class="social"><span></span><span></span><span></span></div>
</footer>
</body>
</html>
```